Order Management User Interface

I need a new design for our order management screens. They need to be end user friendly and contain the data in an easy to read format. These are online orders. I have attached 3 images from the development solution. For now I just need a new UI and ideally would like it delivered in html so we can easily adapt. The screen has multiple tabs to display the different types of data we store. Ideally the end user needs to see customer focused information first.
I have uploaded an example of a different order view that i like.
Industry/Entity Type
Fashion Retail
Coding
Coded - Design and coding required
Number of Pages Required
1 page

```html
<!DOCTYPE html>
<html lang="en">
<head>
<meta charset="utf-8">
<title>Order 9670363 – Order Management</title>
<link rel="stylesheet" href="https://fonts.googleapis.com/css2?family=Poppins:wght@400;500;600;700&display=swap">
<style>
:root{
  --sidebar:#2c5aa6;
  --page:#f4f4f5;
  --card:#ffffff;
  --field:#f4f4f5;
  --ink:#1f2430;
  --muted:#6f7380;
  --line:#e3e4e8;
  --chip:#e4e5e8;
  --save:#9ed46e;
  --refresh:#2a56a0;
  --accent:#e9494d;
  --link:#2a56a0;
}
*{box-sizing:border-box;margin:0;padding:0}
html,body{width:1200px;height:1022px;overflow:hidden}
body{font-family:"Poppins",sans-serif;background:var(--page);color:var(--ink);position:relative}
.sidebar{position:absolute;left:0;top:0;width:58px;height:1022px;background:var(--sidebar)}
.sidebar svg{position:absolute;left:17px;width:24px;height:24px;fill:none;stroke:#fff;stroke-width:1.5;stroke-linecap:round;stroke-linejoin:round}
.topbar{position:absolute;left:58px;top:0;right:0;height:76px;background:#fff;box-shadow:0 2px 6px rgba(0,0,0,.05)}
.topbar h1{position:absolute;left:34px;top:22px;font-size:22px;font-weight:700;letter-spacing:.3px}
.top-item{position:absolute;top:0;height:76px;display:flex;align-items:center;gap:8px;font-size:12.5px;color:var(--muted);font-weight:500}
.top-item svg{fill:none;stroke:var(--ink);stroke-width:1.5}
.divider{position:absolute;top:0;width:1px;height:76px;background:var(--line)}
.avatar{width:45px;height:45px;border-radius:50%;background:linear-gradient(135deg,#7ea7c2,#e0703e)}
.user{color:var(--ink);font-weight:600;font-size:13px}
.crumbs{position:absolute;left:92px;top:111px;display:flex;gap:9px}
.crumb{height:31px;padding:0 9px;display:flex;align-items:center;gap:5px;font-size:10.5px;font-weight:600;border:1px solid #d5d6da;border-radius:3px;background:#fff}
.crumb.active{background:var(--chip);border-color:var(--chip)}
.crumb i{width:10px;height:10px;border-radius:50%;background:var(--ink);position:relative;display:inline-block}
.crumb i::before,.crumb i::after{content:"";position:absolute;left:2px;top:4.5px;width:6px;height:1.2px;background:#fff;transform:rotate(45deg)}
.crumb i::after{transform:rotate(-45deg)}
.card{position:absolute;background:var(--card);border-radius:14px}
.order-card{left:92px;top:172px;width:1071px;height:468px}
.field{position:absolute;width:234px}
.field label{display:block;font-size:10.5px;font-weight:600;letter-spacing:.2px;height:11px;line-height:11px}
.field .input{margin-top:10px;height:36px;background:var(--field);border-radius:3px;display:flex;align-items:center;justify-content:space-between;padding:0 15px 0 18px;font-size:13.5px;color:var(--muted)}
.field .input.pad{padding-left:14px}
.field svg{width:12px;height:14px;fill:none;stroke:var(--ink);stroke-width:1.6}
.authority{position:absolute;left:46px;top:410px;display:flex;align-items:center;gap:9px;font-size:11.5px;font-weight:500}
.check{width:12px;height:12px;border-radius:2px;background:var(--accent);display:flex;align-items:center;justify-content:center}
.btn{position:absolute;top:399px;width:119px;height:35px;border-radius:2px;color:#fff;font-size:12px;font-weight:700;display:flex;align-items:center;justify-content:center;gap:6px}
.btn svg{fill:none;stroke:#fff;stroke-width:1.6}
.btn.save{left:773px;background:var(--save)}
.btn.refresh{left:901px;background:var(--refresh)}
.tabs{position:absolute;left:92px;top:686px;display:flex}
.tab{height:31px;border:1px solid #d5d6da;border-radius:2px;background:#fff;font-size:10.5px;font-weight:600;display:flex;align-items:center;justify-content:center;margin-right:7px}
.tab.active{background:var(--chip);border-color:var(--chip)}
.items-card{left:93px;top:758px;width:1071px;height:300px}
table{position:absolute;left:18px;top:0;border-collapse:collapse;table-layout:fixed;width:1036px}
th{height:51px;font-size:10.5px;font-weight:500;text-align:center;border-bottom:1px solid var(--line);vertical-align:middle;padding-top:2px}
th.left{text-align:left;padding-left:16px}
td{border-left:1px solid var(--line);text-align:center;font-size:11.5px;color:#3a3e48;vertical-align:middle;border-bottom:1px solid var(--line)}
td:first-child{border-left:none;font-size:14px;color:var(--ink)}
td.sku a{color:var(--link);font-weight:600;font-size:12.5px;text-decoration:underline}
.stack{text-align:left;padding-left:10px}
.stack span{display:block;height:27px;line-height:27px;font-size:11.5px}
.stack.values{padding-left:16px;color:#3a3e48}
tr.body-row td{height:187px}
tr.next td{height:40px}
.scroll{position:absolute;left:1059px;top:104px;width:2px;height:80px;background:#d8d9dd}
</style>
</head>
<body>
<nav class="sidebar" aria-label="Main navigation">
  <svg style="top:28px;left:15px;width:28px" viewBox="0 0 28 24"><path d="M2 5h24M2 12h24M2 19h24" stroke-width="2"/></svg>
  <svg style="top:90px" viewBox="0 0 24 24"><path d="M3 5h3l2 10h11l2-7H7"/><circle cx="10" cy="19" r="1.3"/><circle cx="17" cy="19" r="1.3"/></svg>
  <svg style="top:144px" viewBox="0 0 24 24"><rect x="5" y="4" width="14" height="17" rx="2"/><path d="M8 3h8v3H8zM8 10h8M8 13h8M8 16h6"/></svg>
  <svg style="top:198px" viewBox="0 0 24 24"><circle cx="12" cy="12" r="8"/></svg>
  <svg style="top:253px" viewBox="0 0 24 24"><path d="M12 20s-6-6-6-10a6 6 0 0 1 12 0c0 4-6 10-6 10z"/><circle cx="12" cy="10" r="2.2"/><path d="M5 17c-2 1-2 3 7 3s9-2 7-3"/></svg>
  <svg style="top:309px" viewBox="0 0 24 24"><circle cx="11" cy="8" r="4"/><path d="M3 21c0-4 4-7 8-7M15 15h6M15 18h6M15 21h6"/></svg>
  <svg style="top:362px" viewBox="0 0 24 24"><path d="M2 12s4-6 10-6 10 6 10 6-4 6-10 6S2 12 2 12z"/><circle cx="12" cy="12" r="3"/></svg>
  <svg style="top:414px" viewBox="0 0 24 24"><rect x="5" y="11" width="14" height="10" rx="2"/><path d="M8 11V8a4 4 0 0 1 8 0v3M12 15v2"/></svg>
</nav>

<header class="topbar">
  <h1>DEVELOPMENT</h1>
  <div class="top-item" style="left:684px">
    <svg width="30" height="30" viewBox="0 0 30 30"><path d="M8 21V14a7 7 0 0 1 14 0v7l2 2H6z"/><path d="M12 25a3 3 0 0 0 6 0"/><circle cx="15" cy="4" r="2" fill="#8bc34a" stroke="none"/></svg>
    NOTIFICATION
  </div>
  <div class="divider" style="left:832px"></div>
  <div class="top-item" style="left:859px">
    <svg width="24" height="24" viewBox="0 0 24 24"><circle cx="12" cy="12" r="10.5"/><path d="M9.5 9.5a2.5 2.5 0 1 1 3.5 2.3c-.7.3-1 .8-1 1.5v.7"/><circle cx="12" cy="17" r=".6" fill="#1f2430"/></svg>
    HELP
  </div>
  <div class="divider" style="left:943px"></div>
  <div class="top-item" style="left:970px">
    <div class="avatar" role="img" aria-label="User profile photo"></div>
    <span class="user">JOHN DOE</span>
    <svg width="10" height="8" viewBox="0 0 10 8"><path d="M2 2l3 3 3-3" stroke-width="1.6"/></svg>
  </div>
</header>

<div class="crumbs">
  <div class="crumb active">ORDER SEARCH <i></i></div>
  <div class="crumb">ORDER 9670363 <i></i></div>
</div>

<section class="card order-card">
  <div class="field" style="left:46px;top:38px"><label>ORDER NO*</label><div class="input">9670363</div></div>
  <div class="field" style="left:295px;top:38px"><label>BRAND*</label><div class="input">Valenti</div></div>
  <div class="field" style="left:544px;top:38px"><label>ORDER TYPE*</label><div class="input pad">Sale</div></div>
  <div class="field" style="left:793px;top:38px"><label>STATUS*</label><div class="input">New</div></div>

  <div class="field" style="left:46px;top:107px"><label>ORIG ORDER NO*</label><div class="input">9670363</div></div>
  <div class="field" style="left:295px;top:107px"><label>REFERENCE*</label><div class="input">9670363</div></div>
  <div class="field" style="left:544px;top:107px"><label>ORDER CHANNEL*</label><div class="input pad">Standard</div></div>
  <div class="field" style="left:793px;top:107px"><label>LOCATION CODE*</label><div class="input">1301</div></div>

  <div class="field" style="left:46px;top:176px"><label>CUSTOMER NO*</label><div class="input pad">+08 123 456</div></div>
  <div class="field" style="left:295px;top:176px"><label>FIRST NAME*</label><div class="input pad">John</div></div>
  <div class="field" style="left:544px;top:176px"><label>SURNAME*</label><div class="input pad">John doe</div></div>
  <div class="field" style="left:793px;top:176px"><label>EMAIL*</label><div class="input pad">Info@example.com</div></div>

  <div class="field" style="left:46px;top:245px"><label>TOTAL RETAIL*</label><div class="input pad">105.00<svg viewBox="0 0 12 14"><path d="M3 5l3-3 3 3M3 9l3 3 3-3"/></svg></div></div>
  <div class="field" style="left:295px;top:245px"><label>TOTAL TAX*</label><div class="input pad">9.55<svg viewBox="0 0 12 14"><path d="M3 5l3-3 3 3M3 9l3 3 3-3"/></svg></div></div>
  <div class="field" style="left:544px;top:245px"><label>SHIPPING AMOUNT*</label><div class="input pad">0<svg viewBox="0 0 12 14"><path d="M3 5l3-3 3 3M3 9l3 3 3-3"/></svg></div></div>
  <div class="field" style="left:793px;top:245px"><label>SHIPPING TAX*</label><div class="input pad">0<svg viewBox="0 0 12 14"><path d="M3 5l3-3 3 3M3 9l3 3 3-3"/></svg></div></div>

  <div class="field" style="left:46px;top:314px;width:482px"><label>INSTRUCTION*</label><div class="input pad">Type your text...</div></div>
  <div class="field" style="left:547px;top:314px;width:231px"><label>DELIVERY DISCOUNT*</label><div class="input pad">0<svg viewBox="0 0 12 14"><path d="M3 5l3-3 3 3M3 9l3 3 3-3"/></svg></div></div>
  <div class="field" style="left:787px;top:314px;width:235px"><label>CREATED*</label><div class="input pad">21-01-200 02:05 PM</div></div>

  <div class="authority">AUTHORITY TO LEAVE <span class="check"><svg width="8" height="8" viewBox="0 0 8 8"><path d="M1.5 4l1.8 1.8L6.5 2" fill="none" stroke="#fff" stroke-width="1.4"/></svg></span></div>
  <div class="btn save"><svg width="17" height="17" viewBox="0 0 17 17"><path d="M2 2h10l3 3v10H2z"/><path d="M5 2v4h6V2M5 15v-5h7v5"/></svg>SAVE</div>
  <div class="btn refresh"><svg width="24" height="24" viewBox="0 0 24 24"><path d="M20 10a8 8 0 0 0-14.5-3M4 14a8 8 0 0 0 14.5 3"/><path d="M5 3v4h4M19 21v-4h-4"/></svg>REFRESH</div>
</section>

<div class="tabs">
  <div class="tab active" style="width:77px;margin-right:6px">ITEMS</div>
  <div class="tab" style="width:97px;margin-right:8px">CUSTOMER (S)</div>
  <div class="tab" style="width:81px">ADDRESSES</div>
  <div class="tab" style="width:79px">PAYMENTS</div>
  <div class="tab" style="width:81px;margin-right:6px">VOUCHERS</div>
  <div class="tab" style="width:98px">EVENT QUEUES</div>
  <div class="tab" style="width:71px">UPDATES</div>
  <div class="tab" style="width:90px;margin-right:6px">FULFILMENTS</div>
  <div class="tab" style="width:72px">HISTORY</div>
</div>

<section class="card items-card">
  <table>
    <colgroup>
      <col style="width:16px"><col style="width:88px"><col style="width:102px"><col style="width:76px"><col style="width:97px"><col style="width:80px"><col style="width:80px"><col style="width:70px"><col style="width:80px"><col style="width:71px"><col style="width:116px"><col style="width:114px"><col style="width:46px">
    </colgroup>
    <thead>
      <tr>
        <th></th><th>SKU</th><th class="left" colspan="2">PRODUCTS</th><th>IS DROPSHIP</th><th>QUANTITY</th><th>UNIT RETAIL</th><th>UNIT TAX</th><th>DISCOUNT</th><th>FINAL</th><th>DISCOUNT REASON</th><th>COUPON CODE</th><th>STATUS</th>
      </tr>
    </thead>
    <tbody>
      <tr class="body-row">
        <td>+</td>
        <td class="sku"><a>2230566</a></td>
        <td class="stack"><span>Vendor</span><span>Brand</span><span>Product Code</span><span>Description</span><span>Colour (COde)</span><span>Size</span></td>
        <td class="stack values"><span></span><span></span><span>2002589</span><span>PJ SET</span><span>900</span><span>12/14</span></td>
        <td>False</td><td>01</td><td>35.00</td><td>3.18</td><td>0.00</td><td>35.00</td><td></td><td></td><td></td>
      </tr>
      <tr class="next"><td></td><td></td><td></td><td></td><td></td><td></td><td></td><td></td><td></td><td></td><td></td><td></td><td></td></tr>
    </tbody>
  </table>
  <div class="scroll"></div>
</section>
</body>
</html>
```